New design for a company based in SF called Lumo Ride. People rent out our cars and we would like to create a subscription based platform to rent out our cars.
We rent out cars through ride share hub and vexa and would like people to be able to book or be redirected from our site.
Platform
I would like to have three interface.
Here are the things we need;
First interface
Company side where we can custom pricing of level subscription
level one classic; level two premiere; level 3 premium,
Second Interface-
User subscribing to the car
A subscription of low, medium, and premium
-each level needs to be based on how much miles they use per year.
-Insurance selected
This will be a custom delivery service on car
-Provide a drop off time
-minimum 1 hour notice
Third Interface
Peer to Peer Drop off-
Have people who want to get paid and select what car they would like to pick up and drop off
Create algorithm for each price to drop off due to time and distance from it destination
Updates
Need extra days to review
I emailed support and it took them 5 days to respond to find out that the designer who we select for our web design is the same designer for our logo. I need the 5 extra days because I need to fix the logo now. Thank you
Target Market(s)
domestic and international tourists travelling to San Francisco bay area-
Industry/Entity Type
Travel Industry
Logo Text
Either the name Lumo Ride or LR. I would like it to have a message within the Logo. https://www.plorvex.com/learn/hidden-meanings-behind-50-worlds-recognizable-logos/ Similar to Quibly,
Coding
Coded - Design and coding required
Number of Pages Required
1 page
Requirements
Must have
- page with what level subscription they need; Classic; Premiere, Premium
Nice to have
- calendar of availability

```html
<!DOCTYPE html>
<html lang="en">
<head>
<meta charset="utf-8">
<title>Lumo Ride — Rentals Made Easy</title>
<link rel="stylesheet" href="https://fonts.googleapis.com/css2?family=Montserrat:wght@500;600;700;800&family=Open+Sans:wght@400;600;700&display=swap">
<style>
:root{
  --navy:#0d3166;
  --navy-deep:#0a2654;
  --orange:#f7931e;
  --text:#333a45;
  --muted:#6b7280;
  --light:#f4f6f9;
  --green:#7cc242;
  --blue:#1c8fd6;
  --yellow:#fbb03b;
  --white:#ffffff;
}
*{box-sizing:border-box;margin:0;padding:0}
html,body{width:1200px;height:5263px;overflow:hidden}
body{position:relative;background:var(--white);font-family:"Open Sans",sans-serif;color:var(--text)}
.abs{position:absolute}
h1,h2,h3,h4{font-family:"Montserrat",sans-serif}
.accent{color:var(--orange)}

/* header */
.brand{left:40px;top:52px;display:flex;align-items:center;gap:14px}
.brand-dot{width:46px;height:46px;border-radius:50%;background:var(--orange)}
.brand-name{font-family:"Montserrat",sans-serif;font-weight:700;font-size:36px;color:var(--navy)}
.auth{right:44px;top:46px;display:flex;gap:12px}
.pill{font-family:"Montserrat",sans-serif;font-weight:700;font-size:13px;height:32px;width:86px;border-radius:16px;display:flex;align-items:center;justify-content:center}
.pill-solid{background:var(--navy);color:var(--white)}
.pill-line{border:2px solid var(--orange);color:var(--orange)}
.nav{right:44px;top:102px;display:flex;gap:28px;font-family:"Montserrat",sans-serif;font-weight:600;font-size:14px;color:var(--navy)}

/* hero */
.hero-photo{left:585px;top:150px;width:615px;height:515px;border-radius:0 0 0 300px;background:linear-gradient(135deg,#c9b79a,#6e5a48 55%,#2d2a2e);box-shadow:-14px 14px 0 #b9dcee}
.hero-title{left:77px;top:286px;font-weight:700;font-size:46px;color:var(--navy)}
.hero-copy{left:77px;top:356px;width:420px;font-size:19px;line-height:1.45;color:var(--text)}
.btn{font-family:"Montserrat",sans-serif;font-weight:700;color:var(--white);background:var(--orange);border-radius:30px;display:flex;align-items:center;justify-content:center;letter-spacing:.5px}
.hero-btn{left:77px;top:472px;width:318px;height:56px;font-size:19px}
.scroll{left:580px;top:620px;width:40px;text-align:center;font-size:13px;color:var(--muted)}

/* section titles */
.section-title{left:0;width:1200px;text-align:center;font-weight:800;font-size:36px;color:var(--navy)}

/* how it works */
.step-art{width:212px;height:212px;border-radius:50%;border:10px solid var(--white);box-shadow:0 6px 20px rgba(0,0,0,.12)}
.step-text{width:500px}
.step-text h3{font-weight:800;font-size:19px;margin-bottom:6px}
.step-text p{font-size:19px;line-height:1.38}
.step-navy h3{color:var(--navy)}
.step-orange h3{color:var(--orange)}

/* pricing */
.pricing{left:0;top:1912px;width:1200px;height:808px;background:var(--light)}
.plan{top:2106px;width:296px;height:470px;border-radius:150px 150px 36px 36px;border:8px solid var(--white);box-shadow:0 10px 26px rgba(0,0,0,.15);color:var(--white);text-align:center;padding:62px 26px 0}
.plan-classic{left:133px;background:linear-gradient(#8fd14f,#4ea82f)}
.plan-premiere{left:474px;background:linear-gradient(#2fa6e6,#135fb0)}
.plan-premium{left:811px;background:linear-gradient(#ffc52e,#f47b20)}
.plan h3{font-weight:800;font-size:34px;margin-bottom:14px}
.plan-desc{font-size:14px;line-height:1.35;padding-bottom:14px;border-bottom:2px solid rgba(255,255,255,.7)}
.plan ul{list-style:none;text-align:left;font-size:14px;line-height:1.55;margin-top:14px;padding-left:8px}
.plan li::before{content:"• ";}
.price{left:-20px;bottom:-26px;width:140px;height:140px;border-radius:50%;border:10px solid var(--white);display:flex;flex-direction:column;align-items:center;justify-content:center;font-family:"Montserrat",sans-serif;font-weight:800}
.price b{font-size:40px;line-height:1}
.price span{font-size:11px;margin-top:4px}
.plan-classic .price{background:#7cc242}
.plan-premiere .price{background:#36b3e8}
.plan-premium .price{background:#ffc233}
.signup{right:-14px;bottom:32px;width:150px;height:52px;border-radius:8px 0 0 8px;display:flex;align-items:center;justify-content:center;font-family:"Montserrat",sans-serif;font-weight:700;font-size:20px}
.plan-classic .signup{background:#3f9a26}
.plan-premiere .signup{background:#0e4f9a}
.plan-premium .signup{background:#e56c10}

/* faq */
.faq{left:0;top:2720px;width:1200px;height:615px;background:var(--navy)}
.faq-art{left:0;top:2740px;width:520px;height:590px;border-radius:0 40px 0 0;background:linear-gradient(160deg,#2b5a98,#1b417a 60%,#b6a0d8)}
.faq-title{left:95px;top:2812px;font-weight:800;font-size:36px;line-height:1.22;color:var(--white)}
.faq-list{left:527px;top:2812px;width:590px;display:flex;flex-direction:column;gap:13px}
.faq-item{background:var(--white);border-radius:8px;padding:7px 16px;font-family:"Montserrat",sans-serif;font-weight:600;font-size:15px;color:var(--navy);display:flex;justify-content:space-between;align-items:center}
.faq-item .chev{width:22px;height:22px;border-radius:50%;background:#e3e7ee;display:flex;align-items:center;justify-content:center}
.faq-open{flex-direction:column;align-items:stretch}
.faq-open .row{display:flex;justify-content:space-between;align-items:center}
.faq-open p{font-family:"Open Sans",sans-serif;font-weight:400;font-size:14px;line-height:1.42;color:var(--text);margin-top:8px;padding-bottom:6px}

/* testimonials */
.quote{top:3520px;width:318px;height:178px;background:var(--light);padding:22px 26px;font-size:18px;line-height:1.4;text-align:center}
.quote .mark{font-family:"Montserrat",sans-serif;font-weight:800;font-size:38px;line-height:0;color:var(--text);vertical-align:-14px}
.avatar{width:96px;height:96px;border-radius:50%;border:6px solid var(--white);box-shadow:0 4px 14px rgba(0,0,0,.15);background:linear-gradient(#d8c2ae,#8e7664)}
.person{font-family:"Montserrat",sans-serif;font-weight:700;font-style:normal;font-size:18px;color:var(--text)}

/* press */
.press{left:0;top:3924px;width:1200px;height:253px;background:var(--light)}
.press-label{left:0;top:3996px;width:1200px;text-align:center;font-family:"Montserrat",sans-serif;font-weight:800;font-size:15px;color:var(--navy)}
.press-row{left:120px;top:4060px;width:960px;display:flex;justify-content:space-between;align-items:center}
.badge{background:#8a9099;opacity:.75}

/* about */
.about-photo{left:96px;top:4228px;width:362px;height:362px;border-radius:50%;border:10px solid var(--white);box-shadow:0 8px 24px rgba(0,0,0,.15);background:linear-gradient(150deg,#cfe3ef,#8aa4b8 50%,#4d5a62)}
.about-title{left:527px;top:4290px;font-weight:800;font-size:36px;color:var(--navy)}
.about-copy{left:527px;top:4362px;width:580px;font-size:17px;line-height:1.42}
.about-btn{left:527px;top:4586px;width:226px;height:46px;font-size:16px}

/* footer */
.footer{left:0;top:4633px;width:1200px;height:597px;background:var(--navy);color:var(--white)}
.footer-brand{left:0;top:4800px;width:1200px;display:flex;justify-content:center;align-items:center;gap:14px}
.footer-brand .brand-name{color:var(--white);font-size:40px}
.fcol{top:4948px}
.fcol h4{font-weight:800;font-size:14px;margin-bottom:16px;letter-spacing:.4px}
.fcol ul{list-style:none;font-size:14px;line-height:1.6}
.fcol li::before{content:"› ";color:var(--orange)}
.contact-line{display:flex;gap:10px;font-size:14px;line-height:1.5;margin-bottom:14px}
.icon{flex:none;width:22px;height:22px;border-radius:50%;border:1.5px solid var(--white);display:flex;align-items:center;justify-content:center}
.social{display:flex;align-items:center;gap:12px;font-size:15px;margin-bottom:14px}
.social i{width:24px;height:24px;border-radius:4px;background:var(--white);display:block}
.nl-copy{font-size:14px;line-height:1.45;width:270px}
.nl-input{margin-top:14px;width:260px;height:30px;border-radius:15px;background:var(--white);color:var(--muted);font-size:12px;padding:0 14px;display:flex;align-items:center}
.nl-btn{margin-top:10px;width:130px;height:28px;font-size:12px}
.copyright{left:0;top:5230px;width:1200px;height:33px;background:var(--white);text-align:center;font-size:11px;font-weight:600;color:var(--navy);line-height:33px}
</style>
</head>
<body>

<!-- header -->
<div class="abs brand"><span class="brand-dot"></span><span class="brand-name">Lumo Ride</span></div>
<div class="abs auth"><span class="pill pill-solid">SIGN UP</span><span class="pill pill-line">LOGIN</span></div>
<nav class="abs nav"><span>HOW IT WORKS</span><span>PRICING</span><span>FAQs</span><span>ABOUT</span><span>BROWSE CARS</span></nav>

<!-- hero -->
<div class="abs hero-photo" role="img" aria-label="Photo of travellers raising their arms in a vintage convertible at sunset"></div>
<h1 class="abs hero-title">Rentals Made Easy</h1>
<p class="abs hero-copy">Monthly car subscriptions delivered right to your door. Plus, all of our cars come with insurance, maintenance and warranty.</p>
<div class="abs btn hero-btn">GET STARTED</div>
<div class="abs scroll">
  <svg width="24" height="36" viewBox="0 0 24 36"><rect x="2" y="2" width="20" height="32" rx="10" fill="none" stroke="#333a45" stroke-width="2"/><rect x="10.5" y="8" width="3" height="8" rx="1.5" fill="#333a45"/></svg>
  <div>scroll</div>
</div>

<!-- how it works -->
<h2 class="abs section-title" style="top:800px">HOW <span class="accent">IT WORKS</span></h2>

<div class="abs step-art" style="left:140px;top:895px;background:linear-gradient(#6fcadf,#f1a3a8)" role="img" aria-label="Illustration of a hand subscribing on a tablet"></div>
<div class="abs step-text step-navy" style="left:414px;top:955px"><h3>01. SUBSCRIBE ONLINE</h3><p>Lorem ipsum dolor sit amet, consectetur adipiscing elit, sed do eiusmod tempor incididunt ut labore et dolore magna aliqua.</p></div>

<div class="abs step-art" style="left:825px;top:1128px;background:linear-gradient(#f3f3f3,#d84a3a)" role="img" aria-label="Illustration of car keys being handed over beside a red car"></div>
<div class="abs step-text step-orange" style="left:274px;top:1180px"><h3>02. PICK A CAR AND GET IT DELIVERED</h3><p>Lorem ipsum dolor sit amet, consectetur adipiscing elit, sed do eiusmod tempor incididunt ut labore et dolore magna aliqua.</p></div>

<div class="abs step-art" style="left:140px;top:1362px;background:linear-gradient(#7a2a4a,#c8314a)" role="img" aria-label="Illustration of a person driving a red convertible"></div>
<div class="abs step-text step-navy" style="left:414px;top:1415px"><h3>03. DRIVE FULLY COVERED</h3><p>Lorem ipsum dolor sit amet, consectetur adipiscing elit, sed do eiusmod tempor incididunt ut labore et dolore magna aliqua.</p></div>

<div class="abs step-art" style="left:825px;top:1588px;background:linear-gradient(#e2453a,#f08a6a)" role="img" aria-label="Illustration of a hand returning a car key"></div>
<div class="abs step-text step-orange" style="left:274px;top:1648px"><h3>04 RETURN WITH EASE</h3><p>Lorem ipsum dolor sit amet, consectetur adipiscing elit, sed do eiusmod tempor incididunt ut labore et dolore magna aliqua.</p></div>

<!-- pricing -->
<section class="abs pricing"></section>
<h2 class="abs section-title" style="top:2004px">LUMO RIDE <span class="accent">PRICING</span></h2>

<div class="abs plan plan-classic">
  <h3>CLASSIC</h3>
  <p class="plan-desc">Lorem ipsum dolor sit amet, consectetur adipiscing elit, sed do eiusmod tempor.</p>
  <ul><li>Lorem ipsum dolor sit amet</li><li>Consectetur adipiscing elit</li><li>Sed do eiusmod tempor</li><li>Incididunt ut labore et dolo</li></ul>
  <div class="abs price"><b>$30<sup style="font-size:14px">99</sup></b><span>MONTHLY</span></div>
  <div class="abs signup">Sign Up</div>
</div>
<div class="abs plan plan-premiere">
  <h3>PREMIERE</h3>
  <p class="plan-desc">Lorem ipsum dolor sit amet, consectetur adipiscing elit, sed do eiusmod tempor.</p>
  <ul><li>Lorem ipsum dolor sit amet</li><li>Consectetur adipiscing elit</li><li>Sed do eiusmod tempor</li><li>Incididunt ut labore et dolo</li></ul>
  <div class="abs price"><b>$40<sup style="font-size:14px">99</sup></b><span>MONTHLY</span></div>
  <div class="abs signup">Sign Up</div>
</div>
<div class="abs plan plan-premium">
  <h3>PREMIUM</h3>
  <p class="plan-desc">Lorem ipsum dolor sit amet, consectetur adipiscing elit, sed do eiusmod tempor.</p>
  <ul><li>Lorem ipsum dolor sit amet</li><li>Consectetur adipiscing elit</li><li>Sed do eiusmod tempor</li><li>Incididunt ut labore et dolo</li></ul>
  <div class="abs price"><b>$49<sup style="font-size:14px">99</sup></b><span>MONTHLY</span></div>
  <div class="abs signup">Sign Up</div>
</div>

<!-- faq -->
<section class="abs faq"></section>
<div class="abs faq-art" role="img" aria-label="Illustration of a cheerful cartoon host standing beside a lilac convertible"></div>
<h2 class="abs faq-title">FREQUENTLY ASKED<br><span class="accent">QUESTIONS</span></h2>
<div class="abs faq-list">
  <div class="faq-item">Lorem ipsum dolor sit amet?<span class="chev"><svg width="10" height="6"><path d="M1 1l4 4 4-4" stroke="#0d3166" stroke-width="1.6" fill="none"/></svg></span></div>
  <div class="faq-item faq-open">
    <div class="row">Consectetur adipiscing elit, sed do eiusmod tempor incididunt?<span class="chev"><svg width="10" height="6"><path d="M1 5l4-4 4 4" stroke="#0d3166" stroke-width="1.6" fill="none"/></svg></span></div>
    <p>Lorem ipsum dolor sit amet, consectetur adipiscing elit, sed do eiusmod tempor incididunt ut labore et dolore magna aliqua. Ut enim ad minim veniam, quis nostrud exercitation ullamco laboris nisi ut aliquip ex ea commodo consequat. Duis aute irure dolor in reprehenderit in voluptate velit esse cillum dolore eu fugiat nulla pariatur. Excepteur sint occaecat cupidatat non proident, sunt in culpa qui officia deserunt.</p>
  </div>
  <div class="faq-item">Ut enim ad minim veniam?<span class="chev"><svg width="10" height="6"><path d="M1 1l4 4 4-4" stroke="#0d3166" stroke-width="1.6" fill="none"/></svg></span></div>
  <div class="faq-item">Duis aute irure dolor in reprehenderit?<span class="chev"><svg width="10" height="6"><path d="M1 1l4 4 4-4" stroke="#0d3166" stroke-width="1.6" fill="none"/></svg></span></div>
  <div class="faq-item">Excepteur sint occaecat cupidatat non proident?<span class="chev"><svg width="10" height="6"><path d="M1 1l4 4 4-4" stroke="#0d3166" stroke-width="1.6" fill="none"/></svg></span></div>
  <div class="faq-item">Laboris nisi ut aliquip ex ea commodo<span class="chev"><svg width="10" height="6"><path d="M1 1l4 4 4-4" stroke="#0d3166" stroke-width="1.6" fill="none"/></svg></span></div>
</div>

<!-- testimonials -->
<h2 class="abs section-title" style="top:3432px">WHAT <span class="accent">CUSTOMERS SAY</span></h2>

<blockquote class="abs quote" style="left:95px"><span class="mark">“</span> Lorem ipsum dolor sit am et, consectetuer adipiscing elit, sed diam nonummy nibh euismod. <span class="mark">”</span></blockquote>
<div class="abs avatar" style="left:310px;top:3650px" role="img" aria-label="Customer portrait"></div>
<cite class="abs person" style="left:95px;top:3716px">Maren Tolle</cite>

<blockquote class="abs quote" style="left:440px"><span class="mark">“</span> Lorem ipsum dolor sit am et, consectetuer adipiscing elit, sed diam nonummy nibh euismod. <span class="mark">”</span></blockquote>
<div class="abs avatar" style="left:648px;top:3650px" role="img" aria-label="Customer portrait"></div>
<cite class="abs person" style="left:440px;top:3716px">Ilsa Varon</cite>

<blockquote class="abs quote" style="left:782px"><span class="mark">“</span> Lorem ipsum dolor sit am et, consectetuer adipiscing elit, sed diam nonummy nibh euismod. <span class="mark">”</span></blockquote>
<div class="abs avatar" style="left:990px;top:3650px" role="img" aria-label="Customer portrait"></div>
<cite class="abs person" style="left:782px;top:3716px">Theo Brandt</cite>

<!-- press -->
<section class="abs press"></section>
<div class="abs press-label">AS SEEN <span class="accent">ON</span></div>
<div class="abs press-row">
  <span class="badge" style="width:56px;height:36px;border-radius:3px"></span>
  <span class="badge" style="width:130px;height:40px;border-radius:3px"></span>
  <span class="badge" style="width:76px;height:28px;border-radius:3px"></span>
  <span class="badge" style="width:70px;height:70px;border-radius:50%"></span>
  <span class="badge" style="width:90px;height:28px;border-radius:3px"></span>
  <span class="badge" style="width:60px;height:60px;border-radius:50%"></span>
</div>

<!-- about -->
<div class="abs about-photo" role="img" aria-label="Photo of a couple relaxing in the back of an open convertible"></div>
<h2 class="abs about-title">ABOUT <span class="accent">LUMO RIDE</span></h2>
<p class="abs about-copy">Lorem ipsum dolor sit amet, consectetur adipiscing elit, sed do eiusmod tempor incididunt ut labore et dolore magna aliqua. Ut enim ad minim veniam, quis nostrud exercitation ullamco labor is nisi ut aliquip ex ea commodo consequat. Duis aute irure dolor in reprehenderit in voluptate velit esse cillum dolore eu fugiat nulla pariatur. Excepteur sint occaecat cupidatat non proident, sunt in culpa qui officia deserunt mollit anim id est laborum.</p>
<div class="abs btn about-btn">LEARN MORE</div>

<!-- footer -->
<footer class="abs footer"></footer>
<div class="abs footer-brand"><span class="brand-dot"></span><span class="brand-name">Lumo Ride</span></div>

<div class="abs fcol" style="left:77px;color:#fff">
  <h4>QUICK LINKS</h4>
  <ul><li>How it Works</li><li>Pricing</li><li>FAQs</li><li>About</li><li>Browse Cars</li><li>Sign up</li><li>Login</li></ul>
</div>
<div class="abs fcol" style="left:258px;color:#fff">
  <h4>PRICING</h4>
  <ul><li>Classic</li><li>Premiere</li><li>Premium</li></ul>
</div>
<div class="abs fcol" style="left:410px;color:#fff">
  <h4>CONTACT</h4>
  <div class="contact-line"><span class="icon"><svg width="10" height="12" viewBox="0 0 10 12"><path d="M5 11S1 6.8 1 4.3a4 4 0 018 0C9 6.8 5 11 5 11z" fill="#fff"/></svg></span><span>Lumo Ride<br>48 Palvo Lane<br>San Francisco, CA 94110</span></div>
  <div class="contact-line"><span class="icon"><svg width="10" height="10" viewBox="0 0 10 10"><path d="M2 1l2 2-1 1.3a6 6 0 002.7 2.7L7 6l2 2-1.3 1.3C4.6 9 1 5.4.7 2.3z" fill="#fff"/></svg></span><span>+1 555.014.2290</span></div>
  <div class="contact-line"><span class="icon"><svg width="12" height="9" viewBox="0 0 12 9"><rect x=".5" y=".5" width="11" height="8" fill="none" stroke="#fff"/><path d="M.5.5l5.5 4.5L11.5.5" fill="none" stroke="#fff"/></svg></span><span>hello@lumoride.example</span></div>
</div>
<div class="abs fcol" style="left:680px;color:#fff">
  <h4>FOLLOW US</h4>
  <div class="social"><i></i>Friendwall</div>
  <div class="social"><i></i>Chirpline</div>
  <div class="social"><i></i>Snapgrid</div>
</div>
<div class="abs fcol" style="left:870px;color:#fff">
  <h4>NEWSLETTER SUBSCRIPTION</h4>
  <p class="nl-copy">Register your email address to get more information about us</p>
  <div class="nl-input">Email Address</div>
  <div class="btn nl-btn">SUBSCRIBE</div>
</div>

<div class="abs copyright">COPYRIGHT © 2019 LUMO RIDE. ALL RIGHTS RESERVED.</div>

</body>
</html>
```